Surya Namaskar/Sun salutation theme based 12 months desk calendar for 2016 for an indian company

1. We are a corporate support services provider, providing services in Security Management, Fire Safety Management, facility management & HR Services based out of India. pls check website: www.varmilon.co.in
2. Need a complete 12 months desk calendar design layout for 2016 including introductory page & end page,which can then be given for printing straightaway. The calendar should be so designed that when we open any month on the front side, the back side should also give out just the same month dates layout with space to note down any important work on a date etc..All important indian festivals, gazetted hoildays should be mentioned. Any information required can be provided by us
3. Since we give this calendars as part of new year gifts, our calendar has to compete for client desk space with other calendars, it must really be very sophisticated, sleek and attractive
4. Company logo, company contact details, website details and company works must be included in the calendar but in subtle, unobtrusive way. Few details like company logo etc, can be there on all pages.Am uploading some details, rest can be taken from the website, or can be provided
5. Calendar size should be aprx 17 cm * 17 cm including the space needed for spiral. Format should be CDR Ver13 or PDF
6. Theme: Surya Namaskar poses/Sun Salutation poses. These are twelve yoga poses, prescribed for mind /body rejuvenation. Poses 1-12 should be on months Jan16 to Dec 16. A very brief writeup on the same including the relevant mantras may also be included on the page
7. Any query , please mail to rohit.kapadia@varmilon.co.in

Target Market(s)

corporate middle & senior management MNC clients

Industry/Entity Type

Security

Requirements
Must have
• 1.company logos/contact & website details/company works with related photographs.
• 2. surya namaskar poses with a very small brief/health benefit on poses/related mantras
• 3. Indian gazetted holidays & festivals earmarked
• 4. recommendation on the printing paper type & quality/colour of cardboard base & spiral binding
• 5. Attractive Top Introduction page & end page
Nice to have
• 1. photos of the company works
• 2. End page may be used for giving company details in details
• 3. Company logo on each page
• 4. The calendar goes to a variety of corporate clients including hotels, hospitals, shopping malls, manufacturing sector, clubs etc..just for info
• 5. Related photos/same model in all months
• 6. Beautiful Female models in poses
• 7. target audience : 95% male; majority age group: 35-55; middle & senior management
• However, very receptive to any new ideas. The designer has full liberty from our side. The final parameter is that the calendar should be so attractive that it can defeat any other desk calendar competition and win that one spot on the desk
• Any queries/details required, pls mail to rohit.kapadia@varmilon.co.in
Should not have
• Religious overtones

```html
<!DOCTYPE html>
<html lang="en">
<head>
<meta charset="utf-8">
<title>Varmilon Desk Calendar 2016 – January</title>
<link rel="stylesheet" href="https://fonts.googleapis.com/css2?family=Arvo:ital,wght@1,700&family=Josefin+Sans:wght@700&family=Open+Sans:ital,wght@0,400;0,700;1,400&display=swap">
<style>
  :root {
    --cream: #f7e8c9;
    --green: #2a6b5f;
    --orange: #f7a21b;
    --yellow: #f4d42c;
    --sunday: #f2a71e;
    --white: #ffffff;
  }
  html, body {
    margin: 0;
    padding: 0;
    width: 1200px;
    height: 1200px;
    overflow: hidden;
    background: var(--cream);
  }
  .page {
    position: relative;
    width: 1200px;
    height: 1200px;
    background: var(--cream);
    overflow: hidden;
    font-family: "Open Sans", sans-serif;
  }
  .pose-art {
    position: absolute;
    left: 0;
    top: 0;
    width: 1200px;
    height: 1200px;
  }
  .month-name {
    position: absolute;
    top: 36px;
    left: 501px;
    width: 649px;
    margin: 0;
    text-align: center;
    font-family: "Josefin Sans", sans-serif;
    font-weight: 700;
    font-size: 40px;
    line-height: 48px;
    color: var(--sunday);
  }
  .weekdays {
    position: absolute;
    top: 88px;
    left: 501px;
    width: 649px;
    display: grid;
    grid-template-columns: repeat(7, 1fr);
    text-align: center;
    font-weight: 700;
    font-size: 22px;
    line-height: 28px;
    color: var(--green);
  }
  .month-grid {
    position: absolute;
    top: 127px;
    left: 501px;
    width: 649px;
    height: 556px;
    display: grid;
    grid-template-columns: repeat(7, 1fr);
    grid-template-rows: repeat(6, 1fr);
    border-top: 2px solid var(--green);
    border-left: 2px solid var(--green);
    box-sizing: border-box;
  }
  .day {
    border-right: 2px solid var(--green);
    border-bottom: 2px solid var(--green);
    display: flex;
    align-items: center;
    justify-content: center;
    font-family: "Josefin Sans", sans-serif;
    font-weight: 700;
    font-size: 58px;
    color: var(--green);
    padding-top: 10px;
    box-sizing: border-box;
  }
  .day.holiday { color: var(--sunday); }
  .mantra-pill {
    position: absolute;
    left: 420px;
    top: 717px;
    width: 500px;
    height: 156px;
    border-radius: 0 78px 78px 0;
    background: radial-gradient(ellipse at 50% 40%, var(--yellow) 0%, var(--orange) 75%);
  }
  .mantra {
    position: absolute;
    left: 474px;
    top: 730px;
    margin: 0;
    font-family: "Arvo", serif;
    font-style: italic;
    font-weight: 700;
    font-size: 46px;
    line-height: 64px;
    color: var(--green);
  }
  .pose-name {
    position: absolute;
    left: 474px;
    top: 890px;
    margin: 0;
    font-style: italic;
    font-size: 31px;
    line-height: 40px;
    color: var(--green);
  }
  .meaning {
    position: absolute;
    left: 0;
    top: 1048px;
    width: 1200px;
    margin: 0;
    text-align: center;
    font-style: italic;
    font-size: 31px;
    line-height: 40px;
    color: var(--green);
  }
  .footer-band {
    position: absolute;
    left: 0;
    top: 1106px;
    width: 1200px;
    height: 94px;
    background: var(--green);
  }
  .brand {
    position: absolute;
    left: 472px;
    top: 17px;
    display: flex;
    align-items: center;
    gap: 14px;
    color: var(--white);
  }
  .brand-mark {
    width: 48px;
    height: 48px;
    background: var(--white);
  }
  .brand-text { text-align: center; }
  .brand-name {
    font-weight: 700;
    font-size: 25px;
    line-height: 28px;
    letter-spacing: 0.5px;
    text-align: left;
  }
  .brand-line {
    font-size: 11px;
    line-height: 14px;
  }
</style>
</head>
<body>
<main class="page">
  <svg class="pose-art" viewBox="0 0 1200 1200">
    <defs>
      <linearGradient id="sunSwoosh" x1="0" y1="0" x2="1" y2="0">
        <stop offset="0" stop-color="#f7a21b"/>
        <stop offset="1" stop-color="#f4d42c"/>
      </linearGradient>
      <linearGradient id="photoTone" x1="0" y1="0" x2="1" y2="1">
        <stop offset="0" stop-color="#e9e6df"/>
        <stop offset="1" stop-color="#cfcac0"/>
      </linearGradient>
    </defs>
    <path class="sun-swoosh" fill="url(#sunSwoosh)"
          d="M0,940 C120,960 260,980 360,960 C300,1010 160,1035 0,1035 Z"/>
    <path class="frame-band" fill="var(--green)"
          d="M330,0 L392,0 C382,260 432,620 418,840 C408,960 330,990 200,995 C120,998 50,990 0,975 L0,760 Z"/>
    <path class="pose-photo" fill="url(#photoTone)" role="img"
          aria-label="Photograph of a woman standing in the salutation pose, palms joined at the chest, beside a white latticed wall"
          d="M0,0 L340,0 C332,300 372,620 362,780 C356,860 320,885 260,885 C160,885 70,835 0,790 Z"/>
  </svg>

  <h1 class="month-name">JANUARY</h1>
  <div class="weekdays">
    <span>SUN</span><span>MON</span><span>TUE</span><span>WED</span><span>THU</span><span>FRI</span><span>SAT</span>
  </div>
  <div class="month-grid">
    <div class="day"></div><div class="day"></div><div class="day"></div><div class="day"></div><div class="day"></div><div class="day">1</div><div class="day">2</div>
    <div class="day holiday">3</div><div class="day">4</div><div class="day">5</div><div class="day">6</div><div class="day">7</div><div class="day">8</div><div class="day">9</div>
    <div class="day holiday">10</div><div class="day">11</div><div class="day">12</div><div class="day">13</div><div class="day">14</div><div class="day">15</div><div class="day">16</div>
    <div class="day holiday">17</div><div class="day">18</div><div class="day">19</div><div class="day">20</div><div class="day">21</div><div class="day">22</div><div class="day">23</div>
    <div class="day holiday">24</div><div class="day">25</div><div class="day holiday">26</div><div class="day">27</div><div class="day">28</div><div class="day">29</div><div class="day">30</div>
    <div class="day holiday">31</div><div class="day"></div><div class="day"></div><div class="day"></div><div class="day"></div><div class="day"></div><div class="day"></div>
  </div>

  <div class="mantra-pill"></div>
  <p class="mantra">Om<br>Mitraya Namah</p>
  <p class="pose-name">1. Salutation Pose</p>
  <p class="meaning">Prostration to Him who is affectionate to all</p>

  <footer class="footer-band">
    <div class="brand">
      <span class="brand-mark"></span>
      <div class="brand-text">
        <div class="brand-name">VARMILON</div>
        <div class="brand-line">Your trusted partner in safe spaces</div>
        <div class="brand-line">Quality Assured Services</div>
      </div>
    </div>
  </footer>
</main>
</body>
</html>
```